Bold, Captivating, Passion driven brochure design for an Inspirational Speaker and Trainer

I am looking for a brochure design that will immediately draw people into my energy field. It needs to have bold colors yet soft on the eyes. Placement of information is key. I am a Success Navigator and Inspirational Speaker in need of a brochure design that brings who I am and the value I offer to life... needs to jump right off the page.

Target Market(s)

Small business owners and savvy professionals ages 25-45. I am mainly geared towards the beauty industry because that's where I started; however, I want my materials to help me branch out more beyond the beauty industry.

Contact Information for Business Card

Marcus T. Hale, LLC
Marcus T. Hale
Success Navigator & Inspirational Speaker

Font styles to use
Serif

Requirements
Must have
• Cobalt blue is my favorite color... I would like blues of some kind peppered into the color scheme. Needs to look upscale and seasoned in what I do/offer. Serious and yet inviting - not playful but also not too rigid. Essentially, I don't take myself seriously; however, I take what i do very seriously.
Should not have
• Must not look overdone or inauthentic; not traditional and not overly modernized either

```html
<!DOCTYPE html>
<html lang="en">
<head>
<meta charset="utf-8">
<title>Marcus T. Hale — Trifold Brochure</title>
<link href="https://fonts.googleapis.com/css2?family=Lato:wght@400;700&family=Raleway:wght@300;400;600&display=swap" rel="stylesheet">
<style>
  :root{
    --stage:#2e2e30;
    --navy:#1d2a6b;
    --cobalt:#2a4fb8;
    --teal:#1f6f9a;
    --violet:#4a2a8c;
    --magenta:#b2478f;
    --plum:#3a1f4f;
    --band:rgba(60,30,120,.78);
    --ink:#ffffff;
    --ink-soft:rgba(255,255,255,.82);
    --rule:rgba(255,255,255,.85);
    --photo-a:#c9b8a8;
    --photo-b:#8a7567;
  }
  *{box-sizing:border-box;margin:0;padding:0}
  html,body{width:1200px;height:900px;overflow:hidden}
  body{background:var(--stage);font-family:"Lato",Arial,sans-serif;color:var(--ink);position:relative}

  .spread{position:absolute;left:50px;top:150px;width:792px;height:600px;display:flex}
  .panel{position:relative;width:264px;height:600px;padding:34px 24px;overflow:hidden}
  .panel + .panel{border-left:1px solid rgba(255,255,255,.14)}
  .panel--about{background:linear-gradient(170deg,var(--teal) 0%,var(--cobalt) 45%,var(--navy) 100%)}
  .panel--leadership{background:linear-gradient(175deg,var(--teal) 0%,var(--cobalt) 40%,var(--violet) 70%,var(--magenta) 100%)}
  .panel--culture{background:linear-gradient(170deg,var(--teal) 0%,var(--cobalt) 40%,var(--violet) 75%,var(--navy) 100%)}

  .portrait{width:190px;height:200px;margin:0 0 28px 14px;background:linear-gradient(160deg,var(--photo-a),var(--photo-b));border:3px solid rgba(255,255,255,.6)}
  .section-title{font-family:"Raleway",Arial,sans-serif;font-weight:400;font-size:15px;letter-spacing:.08em;text-transform:uppercase;margin-bottom:8px}
  .body-copy{font-size:10.5px;line-height:1.5;color:var(--ink-soft);margin-bottom:12px}
  .testimonial{font-weight:700;font-size:10.5px;line-height:1.45;margin-top:16px}

  .heading-band{display:flex;align-items:center;gap:12px;margin:36px -24px 22px;padding:10px 18px;background:var(--band)}
  .heading-band .icon{flex:0 0 40px;width:40px;height:40px}
  .heading-band h2{font-family:"Raleway",Arial,sans-serif;font-weight:300;font-size:17px;line-height:1.15;letter-spacing:.06em;text-transform:uppercase}

  .discover-list{list-style:none;font-size:10.5px;line-height:1.4;color:var(--ink-soft)}
  .discover-list li{position:relative;padding-left:16px;margin-bottom:4px}
  .discover-list li::before{content:"";position:absolute;left:0;top:3px;width:8px;height:8px;border:1px solid var(--ink)}
  .quote-box{margin-top:40px;padding:12px 0;border-top:1.5px solid var(--rule);border-bottom:1.5px solid var(--rule)}
  .quote-box--tight{margin-top:14px}
  .quote-box .testimonial{margin:0}
  .body-copy--lead{margin-top:18px}
  .keys{list-style:none;font-size:10.5px;line-height:1.45;color:var(--ink-soft)}
  .keys li{margin-bottom:8px}
  .keys strong{color:var(--ink)}

  .cover{position:absolute;left:880px;top:150px;width:270px;height:600px;background:linear-gradient(165deg,var(--violet) 0%,var(--cobalt) 35%,var(--magenta) 70%,var(--plum) 100%);overflow:hidden}
  .brand{margin:22px 20px 0;padding:16px 12px;border:2px solid var(--ink);display:flex;align-items:center;gap:10px}
  .brand .mark{width:12px;height:12px;background:var(--ink);flex:0 0 12px}
  .brand-name{font-family:"Raleway",Arial,sans-serif;font-weight:600;font-size:18px;letter-spacing:.04em;text-transform:uppercase;white-space:nowrap}
  .tagline{font-family:"Raleway",Arial,sans-serif;font-weight:600;font-size:11px;text-align:center;margin-top:10px}
  .hero{position:absolute;left:30px;top:130px;width:210px;height:360px;background:linear-gradient(180deg,#2b2447 0%,#17132a 100%)}
  .cover-footer{position:absolute;left:0;right:0;bottom:0;height:110px;padding:18px 20px;background:rgba(35,20,45,.88)}
  .cover-footer p{font-family:"Raleway",Arial,sans-serif;font-weight:300;font-size:14px;line-height:1.3;letter-spacing:.04em;text-transform:uppercase;text-align:center}
</style>
</head>
<body>

<section class="spread" aria-label="Brochure inside spread">
  <article class="panel panel--about">
    <div class="portrait" role="img" aria-label="Portrait photograph of Marcus T. Hale"></div>
    <h2 class="section-title">Meet Marcus</h2>
    <p class="body-copy">Marcus T. Hale is a Success Navigator committed to unlocking the potential in every leader he meets. His workshops help business owners across the beauty industry and beyond build teams that thrive.</p>
    <p class="body-copy">Marcus has spent over a decade guiding professionals through growth, change and renewal in their careers.</p>
    <p class="testimonial">“Marcus T. Hale is an exceptionally charismatic man who draws people to him. His programs are a huge asset to my business. I highly recommend him to anyone.”</p>
  </article>

  <article class="panel panel--leadership">
    <div class="heading-band">
      <svg class="icon" viewBox="0 0 40 40" aria-hidden="true">
        <circle cx="20" cy="20" r="19" fill="#fff"/>
        <g fill="#3a2a8c"><rect x="16" y="9" width="8" height="6"/><rect x="8" y="25" width="7" height="6"/><rect x="16.5" y="25" width="7" height="6"/><rect x="25" y="25" width="7" height="6"/></g>
        <path d="M20 15v5M11.5 20h17M11.5 20v5M20 20v5M28.5 20v5" stroke="#3a2a8c" stroke-width="1.4" fill="none"/>
      </svg>
      <h2>Leadership<br>Excellence</h2>
    </div>
    <p class="body-copy">Become the business leader you've always wanted to be, one that inspires and empowers greatness in others. Discover the proven strategies used by the greatest business leaders and take your team to the next level in record time.</p>
    <p class="body-copy">You will discover:</p>
    <ul class="discover-list">
      <li>How to effectively communicate your vision</li>
      <li>How to forge a unified purpose</li>
      <li>How to implement lasting balance</li>
      <li>How to create a business culture</li>
      <li>How to develop a winning team</li>
      <li>How to become a leader everyone wants to follow</li>
    </ul>
    <div class="quote-box">
      <p class="testimonial">“If we were a football team Marcus would be our head coach. We would have reached the championship final twice now and would have won.”</p>
    </div>
  </article>

  <article class="panel panel--culture">
    <div class="heading-band">
      <svg class="icon" viewBox="0 0 40 40" aria-hidden="true">
        <circle cx="20" cy="20" r="19" fill="#fff"/>
        <g stroke="#3a2a8c" stroke-width="1.4" fill="none"><circle cx="20" cy="20" r="10"/><ellipse cx="20" cy="20" rx="4.5" ry="10"/><path d="M10 20h20M12 15h16M12 25h16"/></g>
      </svg>
      <h2>Business<br>Culture<br>Excellence</h2>
    </div>
    <p class="body-copy">Learn Marcus's incredible strategies for developing a thriving team culture that keeps your best people engaged, loyal and inspired.</p>
    <div class="quote-box quote-box--tight">
      <p class="testimonial">“Can't even begin to express the gratitude I feel for the workshop and training. Marcus is second to none.”</p>
    </div>
    <p class="body-copy body-copy--lead"><strong>Give your team the edge they need by delivering the three keys for developing a winning culture:</strong></p>
    <ol class="keys">
      <li><strong>1. Engagement</strong> – keep people invested in the mission.</li>
      <li><strong>2. Empathy</strong> – lead with understanding and trust.</li>
      <li><strong>3. Empowerment</strong> – give people room to grow.</li>
    </ol>
  </article>
</section>

<section class="cover" aria-label="Brochure front cover">
  <div class="brand">
    <span class="mark" aria-hidden="true"></span>
    <span class="brand-name">Marcus T. Hale</span>
  </div>
  <p class="tagline">Unleash Your Untapped Potential</p>
  <div class="hero" role="img" aria-label="Photograph of Marcus T. Hale in a dark suit, fist raised"></div>
  <div class="cover-footer">
    <p>Achieve the milestones that matter most to you and take your team to the next level… in record time</p>
  </div>
</section>

</body>
</html>
```